Carver Lindqvist Group Business Cards

We have a new logo, and want to design new business cards with it. We are 21 years in business, and want a fresh but professional look, so not a lot of extra stuff on the card. We are a recruiting and staffing firm focused on placing accounting and finance professionals in the Dallas TX area. I've attached our new logo that should be displayed on the cards. Here is what I think we want on the cards:
Ray Pemberly, CPA
Partner and Managing Director
8282 Orchard Vale Rd.
Suite 610
Dallas, TX 75391
O 214-555-0184
M 214-555-0237
ray@carverlindqvist.example
www.carverlindqvist.example

```html
<!DOCTYPE html>
<html lang="en">
<head>
<meta charset="utf-8">
<title>Carver Lindqvist Group – Business Cards</title>
<link href="https://fonts.googleapis.com/css2?family=Arimo:wght@400;700&display=swap" rel="stylesheet">
<style>
  :root {
    --backdrop: #2b2b2e;
    --card: #ffffff;
    --brand-blue: #2a3f9b;
    --brand-light: #5573c4;
    --stripe-grey: #dcdde2;
    --text-grey: #555760;
  }
  * { box-sizing: border-box; margin: 0; padding: 0; }
  html, body { width: 1200px; height: 880px; overflow: hidden; }
  body {
    background: var(--backdrop);
    font-family: "Arimo", Arial, sans-serif;
    position: relative;
  }
  .card {
    position: absolute;
    width: 620px;
    height: 354px;
    background: var(--card);
    border-radius: 22px;
    overflow: hidden;
    box-shadow: 0 18px 40px rgba(0,0,0,.45);
  }
  .card--front { left: 80px; top: 60px; }
  .card--back { left: 500px; top: 460px; }

  .brand {
    display: flex; align-items: center; gap: 12px;
    color: var(--brand-blue); font-weight: 700; white-space: nowrap;
  }
  .brand__mark { width: 26px; height: 26px; background: var(--brand-blue); flex: none; }

  /* front */
  .card--front .brand { position: absolute; left: 0; right: 0; top: 146px; justify-content: center; font-size: 32px; }
  .front-rule { position: absolute; left: 130px; width: 360px; top: 206px; height: 2px; background: var(--brand-light); }
  .front-url {
    position: absolute; left: 0; right: 0; top: 224px; text-align: center;
    color: var(--brand-blue); font-size: 14px; letter-spacing: 6px;
  }

  /* back */
  .wave { position: absolute; inset: 0; }
  .holder { position: absolute; right: 34px; top: 30px; text-align: right; color: #fff; }
  .holder__name { font-weight: 700; font-size: 20px; }
  .holder__title { font-size: 14px; margin-top: 3px; }

  .card--back .brand { position: absolute; left: 36px; top: 196px; font-size: 24px; }
  .card--back .brand__mark { width: 22px; height: 22px; }
  .back-rule { position: absolute; left: 36px; right: 34px; top: 254px; height: 2px; background: var(--brand-light); }

  .contacts { position: absolute; left: 36px; top: 268px; list-style: none; }
  .contacts li { display: flex; align-items: center; gap: 9px; font-size: 14px; color: var(--text-grey); margin-bottom: 5px; }
  .contacts svg { width: 19px; height: 19px; flex: none; }

  .address { position: absolute; right: 34px; top: 186px; text-align: right; font-size: 14px; line-height: 1.45; color: var(--text-grey); font-style: normal; }
</style>
</head>
<body>

<section class="card card--front" aria-label="Card front">
  <div class="brand"><span class="brand__mark" aria-hidden="true"></span>Carver Lindqvist Group</div>
  <div class="front-rule"></div>
  <p class="front-url">www.carverlindqvist.example</p>
</section>

<section class="card card--back" aria-label="Card back">
  <svg class="wave" viewBox="0 0 620 354" preserveAspectRatio="none" aria-hidden="true">
    <path d="M0,0 H620 V128 C540,196 420,168 300,130 C190,96 80,84 0,112 Z" fill="var(--stripe-grey)" transform="translate(0,16)"/>
    <path d="M0,0 H620 V128 C540,196 420,168 300,130 C190,96 80,84 0,112 Z" fill="var(--brand-light)" transform="translate(0,7)"/>
    <path d="M0,0 H620 V128 C540,196 420,168 300,130 C190,96 80,84 0,112 Z" fill="var(--brand-blue)"/>
  </svg>

  <div class="holder">
    <p class="holder__name">Ray Pemberly, CPA</p>
    <p class="holder__title">Partner and Managing Director</p>
  </div>

  <div class="brand"><span class="brand__mark" aria-hidden="true"></span>Carver Lindqvist Group</div>

  <address class="address">
    8282 Orchard Vale Rd.<br>
    Suite 610<br>
    Dallas, TX 75391
  </address>

  <div class="back-rule"></div>

  <ul class="contacts">
    <li>
      <svg viewBox="0 0 20 20" aria-hidden="true"><circle cx="10" cy="10" r="9" fill="none" stroke="var(--brand-blue)" stroke-width="2"/><path d="M6 7c0 4 3 7 7 7l1-2-2-1-1 1c-1-.5-2-1.5-2.5-2.5l1-1-1-2z" fill="var(--brand-blue)"/></svg>
      214-555-0184
    </li>
    <li>
      <svg viewBox="0 0 20 20" aria-hidden="true"><circle cx="10" cy="10" r="9" fill="none" stroke="var(--brand-blue)" stroke-width="2"/><rect x="7" y="5" width="6" height="10" rx="1" fill="none" stroke="var(--brand-blue)" stroke-width="1.5"/></svg>
      214-555-0237
    </li>
    <li>
      <svg viewBox="0 0 20 20" aria-hidden="true"><circle cx="10" cy="10" r="9" fill="none" stroke="var(--brand-blue)" stroke-width="2"/><rect x="5.5" y="6.5" width="9" height="7" fill="var(--brand-blue)"/><path d="M5.5 6.5l4.5 4 4.5-4" fill="none" stroke="#fff" stroke-width="1"/></svg>
      ray@carverlindqvist.example
    </li>
  </ul>
</section>

</body>
</html>
```